Marwick Jewelers New Website Design

This project is to provide a new design for an existing website. The existing website is marwickjewelers dot com . I have created a overview document that outlines all the details for the project. I do not need the design to be converted into HTML. I have a team for that already so please don't ask. I have a lot of images .. too many to upload here so they are on my dev server located at pinefoxstudio com slash marwick slash assets

Number of Pages Required

1 page

```html
<!DOCTYPE html>
<html lang="en">
<head>
<meta charset="utf-8">
<title>Marwick Jewelers</title>
<link href="https://fonts.googleapis.com/css2?family=Montserrat:wght@400;500;600;700&family=Allura&display=swap" rel="stylesheet">
<style>
:root{
  --teal:#4a8690;
  --teal-dark:#3f7680;
  --ink:#222325;
  --muted:#555a5e;
  --soft:#f3f3f5;
  --card:#ffffff;
  --footer:#111113;
  --rose:#d89a8a;
  --blush:#f4e1dc;
  --silver:#c9cbd1;
  --gold:#d9b56a;
}
*{box-sizing:border-box;margin:0;padding:0}
html,body{width:1200px;height:4478px;overflow:hidden}
body{position:relative;background:#fff;font-family:'Montserrat',sans-serif;color:var(--ink)}
.center-title{position:absolute;left:0;width:1200px;text-align:center;font-weight:700;font-size:19px;letter-spacing:.3px;text-transform:uppercase}
.center-title span{color:var(--teal)}
.rule{position:absolute;left:587px;width:26px;height:2px;background:var(--teal)}
.btn-outline{position:absolute;border:2px solid var(--teal);color:var(--teal);font-size:10px;font-weight:600;text-transform:uppercase;display:flex;align-items:center;justify-content:center;letter-spacing:.3px;background:#fff;white-space:nowrap}
.btn-solid{position:absolute;background:var(--teal);color:#fff;font-size:10.5px;font-weight:600;text-transform:uppercase;display:flex;align-items:center;justify-content:center;letter-spacing:.3px;white-space:nowrap}
.arrow{position:absolute;width:24px;height:24px}
/* header */
.brand{position:absolute;left:130px;top:32px;font-size:20px;font-weight:600;color:var(--ink);display:flex;align-items:center;gap:8px;white-space:nowrap}
.brand i{display:block;width:12px;height:12px;border-radius:50%;background:var(--teal)}
.contact-item{position:absolute;top:24px;display:flex;gap:10px;align-items:center;font-size:12px;line-height:1.35;color:var(--ink);white-space:nowrap}
.contact-item .ic{width:26px;height:26px;border-radius:50%;background:var(--teal);display:flex;align-items:center;justify-content:center;flex:none}
.nav{position:absolute;top:77px;left:256px;display:flex;gap:19px;font-size:11.5px;color:var(--ink);white-space:nowrap}
.nav .on{color:var(--teal);font-weight:700;text-decoration:underline}
/* hero */
.hero{position:absolute;left:0;top:108px;width:1200px;height:532px;
  background:
    radial-gradient(circle at 78% 32%,rgba(255,255,255,.55) 0,rgba(255,255,255,0) 9%),
    radial-gradient(circle at 90% 60%,rgba(255,255,255,.45) 0,rgba(255,255,255,0) 7%),
    radial-gradient(circle at 55% 20%,rgba(255,255,255,.4) 0,rgba(255,255,255,0) 6%),
    radial-gradient(circle at 30% 80%,rgba(255,255,255,.35) 0,rgba(255,255,255,0) 8%),
    radial-gradient(ellipse at 68% 45%,#e6b4a6 0,rgba(230,180,166,0) 35%),
    radial-gradient(ellipse at 28% 78%,#d99c8a 0,rgba(217,156,138,0) 30%),
    linear-gradient(120deg,#efd6d1 0,#f4e4e0 45%,#e8c8c2 100%)}
.hero h1{position:absolute;left:130px;top:72px;font-family:'Allura',cursive;font-weight:400;font-size:74px;color:var(--teal-dark);white-space:nowrap}
.hero p{position:absolute;left:130px;top:167px;font-size:22px;color:#3b3b3d}
.hero-slide-btn{position:absolute;top:250px;width:30px;height:36px;background:#fff;display:flex;align-items:center;justify-content:center}
/* product cards */
.product{position:absolute;top:760px;width:222px;height:346px;background:var(--card);box-shadow:0 2px 8px rgba(0,0,0,.12);text-align:center}
.product .photo{position:absolute;left:20px;top:18px;width:182px;height:175px;border-radius:4px}
.product .name{position:absolute;left:0;width:100%;font-size:12px;line-height:1.45;color:#333}
.product .price{position:absolute;left:0;width:100%;font-size:12.5px;font-weight:700}
.product .btn-solid{left:66px;width:90px;height:27px}
/* repair */
.repair{position:absolute;left:0;top:1224px;width:1200px;height:519px;background:var(--teal);color:#fff;overflow:hidden}
.repair .photo{position:absolute;left:132px;top:33px;width:468px;height:452px;background:radial-gradient(ellipse at 50% 45%,#d9b9a4 0,rgba(217,185,164,0) 30%),linear-gradient(180deg,#3b2f2a 0,#6b5a48 55%,#c9ab7a 100%)}
.repair h2{position:absolute;left:649px;top:56px;font-size:19px;font-weight:700}
.repair .bar{position:absolute;left:649px;top:94px;width:26px;height:2px;background:#fff}
.repair p{position:absolute;left:649px;top:116px;width:370px;font-size:12px;line-height:1.5;opacity:.95}
.repair ul{position:absolute;left:649px;top:200px;list-style:none}
.repair li{font-size:13.5px;font-weight:500;height:30.4px;display:flex;align-items:center;gap:14px;text-transform:uppercase}
.repair li::before{content:"";border-left:5px solid #fff;border-top:4px solid transparent;border-bottom:4px solid transparent}
.repair .btn-light{position:absolute;left:650px;top:430px;width:115px;height:36px;background:#fff;color:var(--teal);font-size:11px;font-weight:700;display:flex;align-items:center;justify-content:center}
.repair .ring-deco{position:absolute;left:1030px;top:300px;width:260px;height:260px;border-radius:50%;border:14px solid rgba(255,255,255,.12)}
/* gifts */
.gift{position:absolute;top:1854px;width:296px;height:320px;background:#f0f0f3}
.gift .photo{position:absolute;left:34px;top:24px;width:228px;height:230px}
.gift .label{position:absolute;top:280px;left:0;width:100%;text-align:center;font-size:13.5px;font-weight:500}
/* engraving */
.band{position:absolute;left:0;width:1200px;background:var(--soft)}
.engrave{position:absolute;top:2400px;width:222px}
.engrave .photo{height:282px}
.engrave .label{margin-top:22px;text-align:center;font-size:13.5px;font-weight:500;text-transform:uppercase}
.engrave .btn-solid{position:relative;margin:14px auto 0;width:96px;height:27px}
/* showcase */
.tile{position:absolute;top:2915px;width:296px;height:294px}
.tile .tag{position:absolute;top:221px;left:50%;transform:translateX(-50%);background:#fff;border:2px solid var(--teal);font-size:15px;font-weight:500;text-transform:uppercase;padding:4px 22px;white-space:nowrap}
/* resources */
.post{position:absolute;top:3435px;width:456px;height:269px;background:#fff;box-shadow:0 2px 8px rgba(0,0,0,.1)}
.post .photo{position:absolute;left:0;top:0;width:216px;height:269px}
.post h3{position:absolute;left:249px;top:24px;width:180px;font-size:14.5px;font-weight:600;line-height:1.3}
.post p{position:absolute;left:249px;top:106px;width:180px;font-size:11.5px;line-height:1.55;color:#444}
.post .btn-solid{left:249px;top:216px;width:96px;height:28px}
/* gallery */
.shot{position:absolute;top:3866px;width:229px;height:259px}
.g-arrow{position:absolute;top:3978px;width:30px;height:34px;background:#fff;display:flex;align-items:center;justify-content:center}
/* footer */
.footer{position:absolute;left:0;top:4135px;width:1200px;height:343px;background:var(--footer);color:#fff}
.footer .f-brand{position:absolute;left:130px;top:120px;font-size:26px;font-weight:600;display:flex;align-items:center;gap:10px;white-space:nowrap}
.footer .f-brand i{width:14px;height:14px;border-radius:50%;background:#fff;display:block}
.footer h4{position:absolute;top:42px;font-size:13px;font-weight:700;text-transform:uppercase}
.f-contact{position:absolute;left:412px;display:flex;gap:14px;align-items:flex-start;font-size:11.5px;line-height:1.45}
.f-contact .ic{width:22px;height:22px;border-radius:50%;background:#fff;flex:none;margin-top:2px}
.f-menu{position:absolute;left:678px;top:74px;font-size:11.5px;line-height:19.2px}
.social{position:absolute;top:74px;width:38px;height:38px;border-radius:50%;background:#fff}
.f-rule{position:absolute;left:130px;top:247px;width:938px;height:1px;background:#3a3a3d}
.hours{position:absolute;top:279px;font-size:12.5px;line-height:1.55}
</style>
</head>
<body>

<header>
  <div class="brand"><i></i>Marwick Jewelers</div>
  <div class="contact-item" style="left:605px">
    <div class="ic"><svg width="12" height="14" viewBox="0 0 12 14"><path d="M6 0a5 5 0 0 0-5 5c0 4 5 9 5 9s5-5 5-9a5 5 0 0 0-5-5zm0 7a2 2 0 1 1 0-4 2 2 0 0 1 0 4z" fill="#fff"/></svg></div>
    <div>48 Elm Ave N,<br>Linden Falls, MN</div>
  </div>
  <div class="contact-item" style="left:770px">
    <div class="ic"><svg width="13" height="13" viewBox="0 0 14 14"><path d="M3 1l2 3-1.5 1.5a8 8 0 0 0 5 5L10 9l3 2-1 2.5C6 14 0 8 .5 2z" fill="#fff"/></svg></div>
    <div>Toll Free<br><span style="font-size:14px">877-555-0148</span></div>
  </div>
  <div class="contact-item" style="left:933px">
    <div class="ic"><svg width="13" height="13" viewBox="0 0 14 14"><path d="M3 1l2 3-1.5 1.5a8 8 0 0 0 5 5L10 9l3 2-1 2.5C6 14 0 8 .5 2z" fill="#fff"/></svg></div>
    <div>Phone<br><span style="font-size:14px">763-555-0192</span></div>
  </div>
  <nav class="nav">
    <span class="on">Company</span><span>Cstom Jewelery Services</span><span>Jewelery Repair Services</span><span>Resources</span><span>Showcase</span><span>Gallery</span><span>Engraving &amp; Trophies</span><span>Gift Ideas</span>
  </nav>
</header>

<section class="hero" role="img" aria-label="Rose gold bracelets and gemstone rings on a soft pink bokeh background">
  <h1>Say It with a Stone</h1>
  <p>and leave her speechless</p>
  <div class="btn-solid" style="left:134px;top:222px;width:115px;height:35px;font-size:11px">Read More</div>
  <div class="hero-slide-btn" style="left:0"><svg width="10" height="14"><path d="M8 1L2 7l6 6" stroke="#999" fill="none" stroke-width="1.5"/></svg></div>
  <div class="hero-slide-btn" style="left:1170px"><svg width="10" height="14"><path d="M2 1l6 6-6 6" stroke="#999" fill="none" stroke-width="1.5"/></svg></div>
</section>

<section>
  <h2 class="center-title" style="top:679px">Featured <span>Products</span></h2>
  <div class="rule" style="top:718px"></div>
  <svg class="arrow" style="left:66px;top:920px" viewBox="0 0 24 24"><path d="M16 2L6 12l10 10" stroke="#888" fill="none" stroke-width="2"/></svg>
  <svg class="arrow" style="left:1110px;top:920px" viewBox="0 0 24 24"><path d="M8 2l10 10L8 22" stroke="#888" fill="none" stroke-width="2"/></svg>

  <div class="product" style="left:130px">
    <div class="photo" role="img" aria-label="Gold solitaire pendant with oval diamond" style="background:radial-gradient(ellipse 30% 48% at 50% 50%,#e2c27a 0,#eadbb6 45%,rgba(255,255,255,0) 100%),#fff"></div>
    <div class="name" style="top:245px">Solitaire Pendant</div>
    <div class="price" style="top:266px">$51.00–$714.00</div>
    <div class="btn-solid" style="top:296px">Contact Us</div>
  </div>
  <div class="product" style="left:369px">
    <div class="photo" role="img" aria-label="Pair of diamond anniversary bands" style="background:radial-gradient(ellipse 48% 32% at 50% 52%,#b9bcc3 0,#dfe0e4 50%,rgba(255,255,255,0) 100%),#fff"></div>
    <div class="name" style="top:200px">Flexible Shared Prong<br>Set Anniversary Bands</div>
    <div class="price" style="top:256px">$51.00–$714.00</div>
    <div class="btn-solid" style="top:286px">Contact Us</div>
  </div>
  <div class="product" style="left:607px">
    <div class="photo" role="img" aria-label="Halo-style semi-set engagement rings" style="background:radial-gradient(ellipse 46% 38% at 50% 52%,#8f939b 0,#cfd1d6 50%,rgba(255,255,255,0) 100%),#fff"></div>
    <div class="name" style="top:200px">Round-Shape Halo-Style<br>Semi-Set Engagement Rings</div>
    <div class="price" style="top:256px">$51.00–$714.00</div>
    <div class="btn-solid" style="top:286px">Contact Us</div>
  </div>
  <div class="product" style="left:845px">
    <div class="photo" role="img" aria-label="Bezel-set gold stud earrings" style="background:radial-gradient(ellipse 42% 20% at 50% 54%,#dcb86a 0,#efe0bd 50%,rgba(255,255,255,0) 100%),#fff"></div>
    <div class="name" style="top:200px">Bezel-Set<br>Stud Earrings</div>
    <div class="price" style="top:256px">$27.00–$583.00</div>
    <div class="btn-solid" style="top:286px">Contact Us</div>
  </div>
  <div class="btn-outline" style="left:522px;top:1143px;width:153px;height:36px">View All Products</div>
</section>

<section class="repair">
  <div class="photo" role="img" aria-label="Rose gold diamond ring displayed on a stand in the store"></div>
  <div class="ring-deco"></div>
  <h2>JEWELERY REPAIR SERVICES</h2>
  <div class="bar"></div>
  <p>Jewelry was meant to be worn, not sit in a drawer. Bring your broken rings, necklaces, earrings and watches to your trusted hometown jeweler.</p>
  <ul>
    <li>Sizing</li><li>Diamond Setting</li><li>Custom Design</li><li>Watch Repairs and Batteries</li><li>Free Ring Cleaning and Inspection</li><li>Engraving</li><li>Appraisals</li>
  </ul>
  <div class="btn-light">READ MORE</div>
</section>

<section>
  <h2 class="center-title" style="top:1784px">Gift <span>Ideas</span></h2>
  <div class="rule" style="top:1822px"></div>
  <div class="gift" style="left:132px"><div class="photo" role="img" aria-label="Boxed cake knife and server set" style="background:linear-gradient(160deg,#2d4f7e 0,#2d4f7e 35%,#e7e3d4 36%,#cfcab8 100%)"></div><div class="label">2pc Cake Serving Set</div></div>
  <div class="gift" style="left:452px"><div class="photo" role="img" aria-label="Wooden cross with gold inlay" style="background:radial-gradient(ellipse 22% 48% at 50% 50%,#7a2a22 0,#a0523f 50%,rgba(240,240,243,0) 100%),#f0f0f3"></div><div class="label">5 Inch Rose Finish Wood</div></div>
  <div class="gift" style="left:772px"><div class="photo" role="img" aria-label="Silver double anniversary photo frame" style="background:radial-gradient(ellipse 50% 44% at 50% 50%,#a9a9ad 0,#d9d9dc 60%,rgba(240,240,243,0) 100%),#f0f0f3"></div><div class="label">ANNIVERSARY FRAME</div></div>
  <div class="btn-outline" style="left:522px;top:2207px;width:153px;height:35px">View All Gift Ideas</div>
</section>

<section class="band" style="top:2292px;height:515px"></section>
<section>
  <h2 class="center-title" style="top:2323px">Engraving <span>&amp; Trophies</span></h2>
  <div class="rule" style="top:2361px"></div>
  <svg class="arrow" style="left:66px;top:2537px" viewBox="0 0 24 24"><path d="M16 2L6 12l10 10" stroke="#888" fill="none" stroke-width="2"/></svg>
  <svg class="arrow" style="left:1110px;top:2537px" viewBox="0 0 24 24"><path d="M8 2l10 10L8 22" stroke="#888" fill="none" stroke-width="2"/></svg>
  <div class="engrave" style="left:130px"><div class="photo" role="img" aria-label="Engraved acrylic trophy with blue base" style="background:linear-gradient(160deg,#3a3f55 0,#8f93a8 50%,#2a4fbf 100%)"></div><div class="label">Acrylic Trophy</div><div class="btn-solid">Contact Us</div></div>
  <div class="engrave" style="left:369px"><div class="photo" role="img" aria-label="Acrylic trophy with colorful emblem" style="background:linear-gradient(160deg,#2c2c2e 0,#b9a98a 50%,#3a3a3c 100%)"></div><div class="label">Acrylic Trophy</div><div class="btn-solid">Contact Us</div></div>
  <div class="engrave" style="left:607px"><div class="photo" role="img" aria-label="Silver bar pendant engraved with a heartbeat line" style="background:linear-gradient(180deg,#e8e8ea 0,#8b8b90 60%,#2b2b2e 100%)"></div><div class="label">Bar Pendant with EKG</div><div class="btn-solid">Contact Us</div></div>
  <div class="engrave" style="left:845px"><div class="photo" role="img" aria-label="Four engraved brass medals" style="background:linear-gradient(160deg,#a89a6e 0,#6d6a5e 50%,#b5a77a 100%)"></div><div class="label">Brass Medals</div><div class="btn-solid">Contact Us</div></div>
</section>

<section>
  <h2 class="center-title" style="top:2846px">Showcase</h2>
  <div class="rule" style="top:2884px"></div>
  <div class="tile" style="left:132px;background:linear-gradient(160deg,#e9d3ef 0,#f6eef2 50%,#d6dcf2 100%)" role="img" aria-label="Stack of gold, rose and silver bangles"><div class="tag">Quick Shops</div></div>
  <div class="tile" style="left:452px;background:linear-gradient(160deg,#eeeef1 0,#c9cbd1 100%)" role="img" aria-label="Silver name ring with birthstones"><div class="tag">Rings</div></div>
  <div class="tile" style="left:772px;background:linear-gradient(160deg,#dfeff4 0,#f2f6f8 50%,#d7e6ec 100%)" role="img" aria-label="Rose gold V-shaped diamond pendant"><div class="tag">Pendants</div></div>
  <div class="btn-outline" style="left:522px;top:3241px;width:153px;height:34px">View All Showcase</div>
</section>

<section class="band" style="top:3320px;height:440px"></section>
<section>
  <h2 class="center-title" style="top:3357px">Resources</h2>
  <div class="post" style="left:132px">
    <div class="photo" role="img" aria-label="Close-up of an engraved metal band" style="background:linear-gradient(160deg,#6d6a66 0,#b8b3ad 50%,#4a4744 100%)"></div>
    <h3>Lorem Ipsum is simply dummy text of the printing</h3>
    <p>There are many variations of passages of Lorem Ipsum available, but the majority have suffered alteration in some form.</p>
    <div class="btn-solid">Read More</div>
  </div>
  <div class="post" style="left:609px">
    <div class="photo" role="img" aria-label="Yellow diamond ring with side stones" style="background:linear-gradient(160deg,#4b4a46 0,#d8c46a 50%,#6b6a66 100%)"></div>
    <h3>Lorem Ipsum is simply dummy text of the printing</h3>
    <p>There are many variations of passages of Lorem Ipsum available, but the majority have suffered alteration in some form.</p>
    <div class="btn-solid">Read More</div>
  </div>
</section>

<section>
  <h2 class="center-title" style="top:3792px">Gallery</h2>
  <div class="shot" style="left:9px;background:linear-gradient(160deg,#c9a58a 0,#7a4a6a 60%,#a88a76 100%)" role="img" aria-label="Gemstone dragonfly pendant"></div>
  <div class="shot" style="left:246px;background:linear-gradient(160deg,#9fb4bf 0,#6a4a8a 50%,#d98a7a 100%)" role="img" aria-label="Amethyst and coral ring"></div>
  <div class="shot" style="left:484px;background:linear-gradient(160deg,#a8b8c2 0,#5a3a7a 50%,#e29a86 100%)" role="img" aria-label="Amethyst and coral ring, side view"></div>
  <div class="shot" style="left:722px;background:linear-gradient(160deg,#3a3530 0,#b8985a 50%,#4a4540 100%)" role="img" aria-label="Gold diamond chevron ring"></div>
  <div class="shot" style="left:960px;background:linear-gradient(160deg,#eeeeef 0,#e6c2b0 60%,#f3f3f4 100%)" role="img" aria-label="Rose gold cat pendant"></div>
  <div class="g-arrow" style="left:9px"><svg width="10" height="14"><path d="M8 1L2 7l6 6" stroke="#333" fill="none" stroke-width="1.5"/></svg></div>
  <div class="g-arrow" style="left:1159px"><svg width="10" height="14"><path d="M2 1l6 6-6 6" stroke="#333" fill="none" stroke-width="1.5"/></svg></div>
</section>

<footer class="footer">
  <div class="f-brand"><i></i>Marwick Jewelers</div>
  <h4 style="left:412px">Contact Us</h4>
  <div class="f-contact" style="top:78px"><div class="ic"></div><div>48 Elm Ave N,<br>Linden Falls, MN</div></div>
  <div class="f-contact" style="top:130px"><div class="ic"></div><div>Call Us<br>763-555-0192</div></div>
  <div class="f-contact" style="top:182px"><div class="ic"></div><div>E mail Us<br>info@marwickjewelers.com</div></div>
  <h4 style="left:678px">Menu</h4>
  <div class="f-menu">Company<br>Custom Jewelery Services<br>Jewelery Repair Services<br>Resources<br>Showcase<br>Gallery<br>Engraving &amp; Trophies<br>Gift Ideas</div>
  <h4 style="left:913px">Menu</h4>
  <div class="social" style="left:913px"></div>
  <div class="social" style="left:963px"></div>
  <div class="f-rule"></div>
  <div class="hours" style="left:130px;top:287px;font-weight:700;font-size:12px">STORE HOURS</div>
  <div class="hours" style="left:262px">Monday - Saturday<br>10:00 AM - 9:00 PM</div>
  <div class="hours" style="left:432px">Sunday<br>CLOSED</div>
  <div class="hours" style="left:862px;top:287px;font-size:11.5px">Copyright © 2022 All Rights Reserved</div>
</footer>

</body>
</html>
```